Driving-coach/trainer who wants to inform about the offer and how I can help people to drive more re

I need a flyer that informs potential customers about my offer.

DL size 210 mm x 99 mm, vertical!

I'm a trainer/coach who helps people to drive a car more relaxed, without fear and more confident.

It's a one to one training. I do train people in their own car. It gets people their freedom back to go where and when they like to go by own car...
Updates

Project Deadline Extended Reason: I would like to extend my project... didn't find the time to give feedback because of unexpected other jobs I had to do.Would be great if you could extend my project around 5 more days. THANKS. Added Wednesday, January 4, 2017

Target Market(s)

People (man an woman) who are afraid of driving a car, or are very stressed while driving....

Industry/Entity Type

Life Coaching

Font styles to use
Sans Serif

Colors
acd136

Requirements
Must have
• Page 1:
• -my offer (see text-pdf)
• -three fotos (see attached files "Pixavine") of people who are satisfied with my offer
• Page 2:
• -advantages in the work with me.
• -contact information
• -and a picture of me (see attached file) next to the contact information or the advantages of my work
• -my logo (see attached file) on Page 1 + 2
• -i like a "clear" and structured layout. "Less is more"

```html
<!DOCTYPE html>
<html lang="de">
<head>
<meta charset="utf-8">
<title>Fahrangst-Bewältigungs-Coach – Flyer</title>
<link href="https://fonts.googleapis.com/css2?family=Ubuntu:wght@300;400;700&family=PT+Sans:wght@400;700&family=PT+Sans+Narrow:wght@400;700&display=swap" rel="stylesheet">
<style>
:root{
  --lime:#acd136;
  --lime-pale:#dcebab;
  --logo-green:#5fae35;
  --ink:#1f1f1f;
  --white:#ffffff;
  --stage:#483e3e;
  --photo-warm:#c9a27a;
  --photo-sky:#9fb6a0;
  --photo-yellow:#e6cf2a;
  --photo-light:#e9e7e4;
}
*{margin:0;padding:0;box-sizing:border-box}
html,body{width:1200px;height:1200px;overflow:hidden;background:var(--stage)}
.panel{position:absolute;top:104px;width:468px;height:992px;background:var(--white);overflow:hidden;font-family:"PT Sans",sans-serif;color:var(--ink)}
.panel--front{left:104px}
.panel--back{left:629px}
.panel svg.bg{position:absolute;left:0;top:0}
.abs{position:absolute}
.headline{left:14px;top:22px;font-family:"Ubuntu",sans-serif;font-weight:700;font-size:74px;color:var(--white);letter-spacing:-1px;line-height:1}
.questions{left:16px;top:100px;list-style:none;font-family:"Ubuntu",sans-serif;font-weight:700;font-size:20.5px;line-height:27px;color:var(--white)}
.questions li{padding-left:20px;position:relative;margin-bottom:8px}
.questions li::before{content:"•";position:absolute;left:0}
.teaser{left:14px;top:270px;font-family:"Ubuntu",sans-serif;font-weight:700;font-size:21px;line-height:25px;color:var(--ink)}
.photo{position:absolute;border-radius:50%}
.brand{font-family:"Ubuntu",sans-serif;font-weight:300;color:var(--logo-green)}
.brand__name{font-size:22px;letter-spacing:2.4px;line-height:1}
.brand__role{font-size:16px;letter-spacing:1.9px;margin-top:4px;line-height:1}
.section-title{left:14px;top:508px;font-family:"Ubuntu",sans-serif;font-weight:700;font-size:23px;line-height:25px}
.situations{left:18px;top:562px;width:440px;list-style:none;font-size:13.6px;line-height:18.2px}
.situations li{padding-left:18px;position:relative;margin-bottom:5px}
.situations li::before{content:"•";position:absolute;left:0}
.closing{left:0;width:468px;top:764px;text-align:center;font-family:"Ubuntu",sans-serif;font-weight:700;font-size:21px}
.rule{left:48px;top:795px;width:372px;height:1.5px;background:var(--lime)}
.steps-title{left:0;width:468px;top:803px;text-align:center;font-family:"PT Sans Narrow",sans-serif;font-weight:700;font-size:31px;color:var(--lime)}
.steps-title .num{font-family:"Ubuntu",sans-serif;font-weight:300;font-size:42px;margin-right:8px;vertical-align:-3px}
.step{top:850px;width:133px;height:90px;background:var(--white);border:2px solid var(--lime);border-radius:7px;display:flex;align-items:center;padding-left:10px;gap:7px}
.step__num{font-family:"PT Sans Narrow",sans-serif;font-weight:700;font-size:44px;line-height:1}
.step__text{font-family:"PT Sans Narrow",sans-serif;font-size:16.5px;line-height:19px}
.footnote{left:20px;width:428px;top:953px;text-align:center;font-size:12.3px;line-height:16px;color:var(--white)}
.benefits{left:15px;top:162px;width:440px;list-style:none;font-size:15.6px;line-height:20px}
.benefits li{padding-left:18px;position:relative;margin-bottom:6px}
.benefits li::before{content:"•";position:absolute;left:0}
.contact{left:0;width:468px;top:804px;text-align:center;color:var(--white)}
.contact__label{font-family:"PT Sans",sans-serif;font-weight:700;font-size:18px}
.contact__name{font-family:"PT Sans Narrow",sans-serif;font-weight:700;font-size:40px;line-height:44px}
.contact__line{font-size:16px;color:var(--ink);line-height:22px}
.contact__phone{font-weight:700;font-size:19px;margin-top:6px;display:flex;justify-content:center;align-items:center;gap:8px}
</style>
</head>
<body>

<section class="panel panel--front">
  <svg class="bg" width="468" height="992" viewBox="0 0 468 992">
    <rect width="468" height="400" fill="var(--lime)"/>
    <path d="M0 360 C120 370 250 400 468 470 L468 500 C300 470 150 420 0 400Z" fill="var(--lime-pale)"/>
    <path d="M0 400 C160 400 300 450 468 530 L468 560 C330 520 180 470 0 440Z" fill="var(--white)"/>
    <path d="M150 400 C260 430 380 490 468 560 L468 595 C360 520 250 460 150 400Z" fill="var(--lime-pale)"/>
    <rect y="916" width="468" height="76" fill="var(--lime)"/>
  </svg>

  <h1 class="abs headline">Wollen Sie</h1>
  <ul class="abs questions">
    <li>Fahrangst überwinden?</li>
    <li>Panikattacken beim<br>Autofahren loswerden?</li>
    <li>Oder einfach sicher<br>Autofahren?</li>
  </ul>

  <div class="photo" role="img" aria-label="Foto: lächelnde junge Frau lehnt aus dem Autofenster" style="left:220px;top:188px;width:264px;height:264px;background:radial-gradient(circle at 55% 40%,var(--photo-warm),var(--photo-sky));border:3px solid var(--white)"></div>
  <div class="photo" role="img" aria-label="Foto: entspannte Frau am Steuer eines Cabrios" style="left:110px;top:258px;width:176px;height:176px;background:radial-gradient(circle at 50% 55%,#d9b58e,#6b5a45);border:2px solid var(--lime)"></div>

  <p class="abs teaser">Dann sind<br>Sie hier<br>richtig!</p>

  <div class="abs brand" style="left:14px;top:444px">
    <div class="brand__name">Katrin Almeroth</div>
    <div class="brand__role">Fahrangst-Bewältigungs-Coach</div>
  </div>

  <h2 class="abs section-title">Kommt Ihnen eine dieser<br>Situationen bekannt vor?</h2>
  <ul class="abs situations">
    <li><b>Angst oder Panikattacken</b> begleiten Sie <b>beim Autofahren</b>. Vielleicht <b>vermeiden</b> Sie deshalb das Autofahren komplett. - Sie möchten angstfrei und/oder ohne Panikattacken fahren.</li>
    <li>Sie <b>trauen sich das Autofahren nicht (mehr) zu</b>. - Sie wünschen sich, sicher, entspannt und stressfrei Auto zu fahren.</li>
    <li><b>Autofahren</b> erleben Sie unter <b>hoher Anspannung und Stress</b>. - Sie wünschen sich, Autofahren sicher und entspannt zu erleben.</li>
    <li>Bestimmte Situationen (z.B. <b>Autobahn, Baustellen, Stadtvekehr</b>...) bereiten Ihnen <b>großen Stress</b>. - Sie möchten diese Situationen souveräner meistern.</li>
  </ul>

  <p class="abs closing">Das muss nicht so bleiben!</p>
  <div class="abs rule"></div>
  <h2 class="abs steps-title"><span class="num">3</span>Schritte zur Lösung</h2>

  <div class="abs step" style="left:24px"><span class="step__num">1</span><span class="step__text">Erstgespräch<br>vereinbaren</span></div>
  <div class="abs step" style="left:169px"><span class="step__num">2</span><span class="step__text">Analyse Ihrer<br>individuellen<br>Situation und<br>Zielsetzung</span></div>
  <div class="abs step" style="left:313px"><span class="step__num">3</span><span class="step__text">Individuelles<br>Coaching und<br>Training</span></div>

  <p class="abs footnote">(ggf. Fahrangst-Therapie - als psychotherapeutische Heilpraktikerin bin ich auf Angst- und Panikstörungen spezialisiert)</p>
</section>

<section class="panel panel--back">
  <svg class="bg" width="468" height="992" viewBox="0 0 468 992">
    <circle cx="107" cy="632" r="66" fill="var(--lime)"/>
  </svg>

  <div class="abs brand" style="left:35px;top:74px">
    <div class="brand__name" style="font-size:23px">Katrin Almeroth</div>
    <div class="brand__role" style="font-size:17px">Fahrangst-Bewältigungs-Coach</div>
  </div>

  <ul class="abs benefits">
    <li>über 10 Jahre Erfahrung als Trainerin und Coach im Bereich Fahrsicherheit.</li>
    <li>Als psychotherapeutische Heilpraktikerin bin ich auf Angststörungen und Panikattacken spezialisiert</li>
    <li>100 % auf Sie zugeschnitten: ich hole Sie genau dort ab, wo Sie jetzt stehen und unterstütze Sie in Ihrem Prozess individuell und zielführend.</li>
    <li>Wenn es Ihnen nicht möglich ist, in meine Praxis nach Lindenfeld Nord zu kommen: Mit der mobilen Praxis komme ich auch zu Ihnen.</li>
    <li>Termine sind auch abends und am Wochenende möglich.</li>
  </ul>

  <div class="photo" role="img" aria-label="Foto: gelber Kleinwagen mit Koffern auf dem Dach in einer Wiese" style="left:39px;top:446px;width:196px;height:196px;background:linear-gradient(180deg,#8fb3c9 0%,#7aa36a 38%,var(--photo-yellow) 55%,#b8a24a 100%);border:2px solid var(--white)"></div>

  <div class="abs" role="img" aria-label="Porträtfoto der Trainerin in weißer Bluse" style="left:243px;top:536px;width:225px;height:290px;background:linear-gradient(180deg,var(--white) 0%,var(--photo-light) 40%,#d8d6d3 100%)"></div>

  <svg class="bg" width="468" height="992" viewBox="0 0 468 992" style="top:0">
    <path d="M0 728 C110 720 200 760 290 785 C360 800 420 800 468 798 L468 992 L0 992Z" fill="var(--lime-pale)"/>
    <path d="M0 780 C120 770 220 800 320 804 C390 806 440 800 468 796 L468 992 L0 992Z" fill="var(--white)" opacity=".7"/>
    <path d="M0 800 C150 795 320 820 468 808 L468 992 L0 992Z" fill="var(--lime)"/>
  </svg>

  <div class="abs contact">
    <div class="contact__label">Contact:</div>
    <div class="contact__name">Katrin Almeroth</div>
    <div class="contact__line">Weitere Informationen finden Sie auf:</div>
    <div class="contact__line" style="display:flex;justify-content:center;align-items:center;gap:8px">
      <svg width="14" height="14" viewBox="0 0 14 14" fill="none" stroke="var(--ink)" stroke-width="1.1"><circle cx="7" cy="7" r="6"/><ellipse cx="7" cy="7" rx="2.6" ry="6"/><path d="M1 7h12M2 4h10M2 10h10"/></svg>
      www.fahrangst-coaching-beispiel.de
    </div>
    <div class="contact__line">Oder rufen Sie mich einfach an:</div>
    <div class="contact__phone">
      <svg width="11" height="18" viewBox="0 0 11 18" fill="none" stroke="var(--white)" stroke-width="1.6"><rect x="1" y="1" width="9" height="16" rx="1.5"/><path d="M4 14.5h3"/></svg>
      0151 00 12 34 56
    </div>
  </div>
</section>

</body>
</html>
```